Mental Health care Company in Washington DC

We are a new mental health care services provider in Washington DC. Please look at these sites.
https://marlowbrookpartners.com
https://www.quillstoneinc.com
https://velmarsh-kt.org/
https://www.trivanqx.com
https://www.thelanternofqz.com

```html
<!DOCTYPE html>
<html lang="en">
<head>
<meta charset="utf-8">
<title>Veyra Health Services</title>
<link rel="stylesheet" href="https://fonts.googleapis.com/css2?family=Lexend:wght@400;500;600&family=Montserrat:ital,wght@0,400;0,500;0,600;1,400&display=swap">
<style>
:root{
  --navy:#0c2244;
  --teal:#a5dadb;
  --teal-deep:#7fc6c9;
  --orange:#f4a462;
  --orange-btn:#f29a55;
  --ice:#eef5fb;
  --ink:#14284b;
  --body:#4a5568;
  --white:#ffffff;
}
*{box-sizing:border-box;margin:0;padding:0}
html,body{width:1200px;height:4587px;overflow:hidden}
body{position:relative;font-family:"Montserrat",sans-serif;color:var(--ink);background:var(--white)}
.abs{position:absolute}
h1,h2,h3,.brand{font-family:"Lexend",sans-serif;font-weight:500}
.btn{position:absolute;display:inline-flex;align-items:center;justify-content:center;height:44px;padding:0 22px;border-radius:22px;font-family:"Lexend",sans-serif;font-size:14px;color:var(--white);white-space:nowrap}
.btn-orange{background:var(--orange-btn)}
.btn-teal{background:var(--teal-deep)}
.photo{position:absolute;overflow:hidden}
.para{position:absolute;font-size:15px;line-height:25px;color:var(--body)}
/* header */
.site-header{position:absolute;left:0;top:0;width:1200px;height:103px;border-top:4px solid var(--orange);background:var(--white)}
.brand{position:absolute;color:var(--ink);font-size:34px;letter-spacing:-0.5px;white-space:nowrap}
.main-nav a{position:absolute;top:45px;font-family:"Lexend",sans-serif;font-size:14px;color:var(--ink);text-decoration:none}
.main-nav a.active{color:var(--orange)}
/* hero */
.hero{position:absolute;left:0;top:103px;width:1200px;height:540px;background:var(--teal)}
.hero-photo{left:560px;top:0;width:640px;height:540px;background:linear-gradient(135deg,#d7e2e6 0%,#b9c6cf 45%,#6e86a6 75%,#cfd7dc 100%)}
.hero-kicker{left:127px;top:135px;font-family:"Lexend",sans-serif;font-weight:400;font-size:26px;color:var(--white)}
.hero-title{left:127px;top:170px;font-size:44px;font-weight:600;color:var(--white)}
.hero .para{left:127px;top:240px;width:400px;font-size:16px;line-height:28px;color:var(--white)}
/* welcome */
.welcome{position:absolute;left:0;top:643px;width:1200px;height:643px;background:linear-gradient(90deg,#eceff1 0%,#f7f8f9 45%,#fff 60%)}
.section-title{position:absolute;font-size:38px;line-height:44px;color:var(--ink);font-weight:600}
/* services */
.services{position:absolute;left:0;top:1286px;width:1200px;height:694px;background:var(--navy)}
.eyebrow{position:absolute;font-family:"Lexend",sans-serif;font-size:16px;letter-spacing:2px;color:var(--teal);font-weight:500}
.services h2{position:absolute;left:0;top:115px;width:1200px;text-align:center;font-size:44px;color:var(--white);font-weight:600}
.service-card{position:absolute;top:204px;width:273px}
.service-card .photo{position:relative;width:273px;height:200px;border-radius:26px 36px 26px 36px}
.service-card h3{margin-top:24px;font-size:20px;color:var(--white);font-weight:600}
.service-card p{margin-top:10px;font-size:13px;line-height:19px;color:#dfe6ef}
.service-card .btn{position:relative;margin-top:18px;height:38px;padding:0 16px;font-size:14px}
/* care team */
.care{position:absolute;left:0;top:1980px;width:1200px;height:620px;background:var(--ice)}
/* why */
.why{position:absolute;left:0;top:2600px;width:1200px;height:536px;background:var(--orange)}
.why-photo{left:560px;top:0;width:640px;height:536px;border-radius:300px 0 0 0;background:linear-gradient(120deg,#e6d3b6 0%,#c89a4c 40%,#4b7a4f 65%,#e7c46d 100%)}
/* testimonials */
.testimonials{position:absolute;left:0;top:3136px;width:1200px;height:555px;background:var(--white)}
.testimonials h2{position:absolute;left:0;top:110px;width:1200px;text-align:center;font-size:38px;font-weight:600;color:var(--ink)}
.quote-card{position:absolute;top:197px;width:298px;height:262px;border-radius:32px;background:var(--teal);padding:32px 36px;color:var(--white)}
.quote-card p{font-style:italic;font-size:14px;line-height:21px}
.quote-card .who{margin-top:26px;font-family:"Lexend",sans-serif;font-size:13px}
.stars{margin-top:8px;display:flex;gap:3px}
/* appointment */
.appointment{position:absolute;left:0;top:3691px;width:1200px;height:484px;background:var(--navy)}
.appointment h2{position:absolute;left:685px;top:105px;font-size:46px;line-height:56px;color:var(--white);font-weight:600}
.appointment .para{left:685px;top:230px;width:400px;color:var(--white);font-size:18px;line-height:28px}
/* footer */
.site-footer{position:absolute;left:0;top:4175px;width:1200px;height:412px;background:var(--white)}
.footer-col h4{position:absolute;top:82px;font-family:"Lexend",sans-serif;font-size:20px;font-weight:600;color:var(--ink)}
.footer-list{position:absolute;top:128px;list-style:none;font-size:15px;line-height:32px;color:var(--body)}
.contact-row{position:absolute;left:823px;display:flex;gap:14px;font-size:14px;line-height:17px;color:var(--body)}
.contact-icon{width:34px;height:34px;border-radius:6px;background:var(--orange);display:flex;align-items:center;justify-content:center;flex:none}
.social{position:absolute;top:284px;width:32px;height:32px;border-radius:4px;background:var(--teal-deep)}
.legal{position:absolute;left:0;top:358px;width:1200px;text-align:center;font-size:14px;color:var(--body)}
</style>
</head>
<body>

<header class="site-header">
  <div class="brand" style="left:86px;top:24px;font-size:30px">Veyra Health</div>
  <nav class="main-nav">
    <a class="active" style="left:375px">Home</a>
    <a style="left:462px">About Us</a>
    <a style="left:575px">Therapies &amp; Treatment</a>
    <a style="left:786px">Our Services</a>
    <a style="left:923px">Gallery</a>
    <a style="left:1020px">Contact Us</a>
  </nav>
</header>

<section class="hero">
  <div class="photo hero-photo" role="img" aria-label="Photo of a therapist comforting a distressed client on a sofa"></div>
  <div class="abs hero-kicker">Veyra Health Services</div>
  <h1 class="abs hero-title">We Care. For You.</h1>
  <p class="para">Lorem ipsum dolor sit amet, consectetur adipiscing elit, sed do eiusmod tempor incididunt ut labore et dolore.</p>
  <span class="btn btn-orange" style="left:127px;top:352px">Make an Appointment</span>
</section>

<section class="welcome">
  <div class="photo" style="left:0;top:0;width:330px;height:643px;background:linear-gradient(90deg,#dfe3e4,#f1f3f4)" role="img" aria-label="Soft background photo of a woman in a bright room"></div>
  <div class="photo" style="left:128px;top:80px;width:467px;height:467px;border-radius:36px;background:linear-gradient(135deg,#8fb0d0 0%,#b49a86 35%,#d8c2b0 60%,#4b5a5c 100%)" role="img" aria-label="Photo collage of therapy sessions, a resting child, clasped hands and a worried young woman"></div>
  <h2 class="section-title" style="left:707px;top:170px">Welcome to<br>Veyra Health Services</h2>
  <p class="para" style="left:717px;top:275px;width:360px">Lorem ipsum dolor sit amet, consectetur adip iscing elit, sed do eiusmod tempor incididunt ut labore et dolore magna aliqua. Quis ipsum suspendisse ultrices gravida. Risus commodo viverra maecenas accumsan lacus vel facilisis.</p>
  <span class="btn btn-teal" style="left:717px;top:447px;width:145px">Read More</span>
</section>

<section class="services">
  <div class="eyebrow" style="left:0;top:84px;width:1200px;text-align:center">OUR SERVICES</div>
  <h2>Tailored Solutions for Every Need</h2>
  <div class="service-card" style="left:127px">
    <div class="photo" style="border:3px solid var(--teal);background:linear-gradient(135deg,#c7b3a0,#6f5646 60%,#4f6f93)" role="img" aria-label="Photo of a person with clasped hands"></div>
    <h3>Behavioral Health</h3>
    <p>Lorem ipsum dolor sit amet, conse ctetur adipiscing elit, sed do eiusm od tempor incididunt ut.</p>
    <span class="btn btn-orange">Read More</span>
  </div>
  <div class="service-card" style="left:463px">
    <div class="photo" style="background:linear-gradient(135deg,#d9d6cf,#9a8d7c 50%,#7a5445)" role="img" aria-label="Photo of a counsellor talking with an older client"></div>
    <h3>Individual Therapy</h3>
    <p>Lorem ipsum dolor sit amet, conse ctetur adipiscing elit, sed do eiusm od tempor incididunt ut.</p>
    <span class="btn btn-orange">Read More</span>
  </div>
  <div class="service-card" style="left:800px">
    <div class="photo" style="background:linear-gradient(135deg,#dfe2e4,#8fa0ae 45%,#c99e78)" role="img" aria-label="Photo of a doctor with a child and parent"></div>
    <h3>Psychiatric Consultations</h3>
    <p>Lorem ipsum dolor sit amet, conse ctetur adipiscing elit, sed do eiusm od tempor incididunt ut.</p>
    <span class="btn btn-orange">Read More</span>
  </div>
</section>

<section class="care">
  <div class="photo" style="left:113px;top:137px;width:214px;height:252px;border-radius:0 0 0 120px;background:linear-gradient(135deg,#efe3da,#c9a897)" role="img" aria-label="Photo of a caregiver holding an elderly hand"></div>
  <div class="abs" style="left:127px;top:408px;width:200px;height:102px;border-radius:100px 100px 0 0;background:var(--teal)"></div>
  <div class="photo" style="left:338px;top:135px;width:308px;height:362px;border-radius:154px 154px 0 0;background:linear-gradient(135deg,#e6ebe4,#b6c1b0 45%,#5f7393)" role="img" aria-label="Photo of a smiling young woman in a counselling session"></div>
  <h2 class="section-title" style="left:707px;top:177px">Your Care Team</h2>
  <p class="para" style="left:717px;top:240px;width:360px">Lorem ipsum dolor sit amet, consectetur adip iscing elit, sed do eiusmod tempor incididunt ut labore et dolore magna aliqua. Quis ipsum suspendisse ultrices gravida. Risus commodo viverra maecenas accumsan lacus vel facilisis.</p>
  <span class="btn btn-orange" style="left:717px;top:405px">Make an Appointment</span>
</section>

<section class="why">
  <div class="photo why-photo" role="img" aria-label="Photo of a mother and daughter embracing"></div>
  <div class="abs" style="left:127px;top:134px;font-family:'Lexend',sans-serif;font-size:13px;color:var(--white)">YOUR CHOICE IS RIGHT HERE</div>
  <h2 class="abs" style="left:127px;top:155px;font-size:38px;font-weight:600;color:var(--white)">Why Choose Us?</h2>
  <p class="para" style="left:127px;top:215px;width:360px;color:var(--white)">Lorem ipsum dolor sit amet, consectetur adip iscing elit, sed do eiusmod tempor incididunt ut labore et dolore magna aliqua. Quis ipsum suspendisse ultrices gravida. Risus commodo viverra maecenas accumsan lacus vel facilisis.</p>
  <span class="btn btn-teal" style="left:127px;top:387px;width:132px">Read More</span>
</section>

<section class="testimonials">
  <h2>Client Testimonials</h2>
  <div class="quote-card" style="left:127px">
    <p>Lorem ipsum doreolor sit ame consectetur adipiscing elit sed do eiusmod tempor incididunt ut labore et dol ore magna aliquaus ipsum suspendisse avida.</p>
    <div class="who">-MARA TELLEN</div>
    <div class="stars"><svg width="60" height="10" viewBox="0 0 60 10"><g fill="#fff"><circle cx="5" cy="5" r="4"/><circle cx="17" cy="5" r="4"/><circle cx="29" cy="5" r="4"/><circle cx="41" cy="5" r="4"/><circle cx="53" cy="5" r="4"/></g></svg></div>
  </div>
  <div class="quote-card" style="left:451px">
    <p>Lorem ipsum doreolor sit ame consectetur adipiscing elit sed do eiusmod tempor incididunt ut labore et dol ore magna aliquaus ipsum suspendisse avida.</p>
    <div class="who">-MARA TELLEN</div>
    <div class="stars"><svg width="60" height="10" viewBox="0 0 60 10"><g fill="#fff"><circle cx="5" cy="5" r="4"/><circle cx="17" cy="5" r="4"/><circle cx="29" cy="5" r="4"/><circle cx="41" cy="5" r="4"/><circle cx="53" cy="5" r="4"/></g></svg></div>
  </div>
  <div class="quote-card" style="left:773px">
    <p>Lorem ipsum doreolor sit ame consectetur adipiscing elit sed do eiusmod tempor incididunt ut labore et dol ore magna aliquaus ipsum suspendisse avida.</p>
    <div class="who">-MARA TELLEN</div>
    <div class="stars"><svg width="60" height="10" viewBox="0 0 60 10"><g fill="#fff"><circle cx="5" cy="5" r="4"/><circle cx="17" cy="5" r="4"/><circle cx="29" cy="5" r="4"/><circle cx="41" cy="5" r="4"/><circle cx="53" cy="5" r="4"/></g></svg></div>
  </div>
</section>

<section class="appointment">
  <div class="photo" style="left:125px;top:30px;width:295px;height:178px;border-radius:150px 150px 0 0;background:linear-gradient(135deg,#e4d3c6,#b48c74)" role="img" aria-label="Photo of two hands held together"></div>
  <div class="photo" style="left:117px;top:234px;width:208px;height:230px;border-radius:0 0 104px 104px;background:linear-gradient(135deg,#d7ddd2,#8ea08a 50%,#5a6a80)" role="img" aria-label="Photo of a therapy session in a bright room"></div>
  <div class="photo" style="left:352px;top:218px;width:168px;height:176px;border-radius:84px 84px 0 0;background:linear-gradient(135deg,#efe6dc,#c6a98f)" role="img" aria-label="Photo of a smiling family"></div>
  <h2>Make an<br>Appointment</h2>
  <p class="para">Lorem ipsum dolor sit amet, consectetur adipiscing elit, sed do eiusmod tempor incididunt ut labore et dolore.</p>
  <span class="btn btn-orange" style="left:685px;top:336px;width:210px">Make an Appointment</span>
</section>

<footer class="site-footer">
  <div class="brand" style="left:127px;top:65px;font-size:28px">Veyra Health</div>
  <p class="para" style="left:127px;top:132px;width:240px;font-size:14px;line-height:21px">Lorem ipsum dolor sit amelot consectetur adipiscing ellorit sed do eiusmod tempor cid idunt ut labore et.</p>
  <span class="social" style="left:176px" role="img" aria-label="Social profile"></span>
  <span class="social" style="left:220px" role="img" aria-label="Social profile"></span>

  <div class="footer-col">
    <h4 style="left:437px">Menu</h4>
    <ul class="footer-list" style="left:437px"><li>Home</li><li>Our Services</li><li>Insurance</li><li>Testimonials</li><li>About</li><li>Contact</li></ul>
  </div>
  <div class="footer-col">
    <h4 style="left:600px">Services</h4>
    <ul class="footer-list" style="left:600px"><li>Medical Services</li><li>Behavioral Health</li><li>Human Services</li><li>Spiritual Needs</li><li>Other Services</li></ul>
  </div>
  <div class="footer-col">
    <h4 style="left:823px">Contact</h4>
  </div>
  <div class="contact-row" style="top:130px">
    <span class="contact-icon"><svg width="18" height="18" viewBox="0 0 24 24" fill="none" stroke="#fff" stroke-width="2"><path d="M12 22s7-7 7-12a7 7 0 0 0-14 0c0 5 7 12 7 12z"/><circle cx="12" cy="10" r="2.5"/></svg></span>
    <span>Veyra Health Services<br>Lindell Ave 12, Washington, DC 20001</span>
  </div>
  <div class="contact-row" style="top:186px">
    <span class="contact-icon"><svg width="18" height="18" viewBox="0 0 24 24" fill="none" stroke="#fff" stroke-width="2"><path d="M5 3h4l2 5-2.5 1.5a11 11 0 0 0 6 6L16 13l5 2v4a2 2 0 0 1-2 2A16 16 0 0 1 3 5a2 2 0 0 1 2-2z"/></svg></span>
    <span>Phone:<br>555 0142 318</span>
  </div>
  <div class="contact-row" style="top:240px">
    <span class="contact-icon"><svg width="18" height="18" viewBox="0 0 24 24" fill="none" stroke="#fff" stroke-width="2"><rect x="3" y="5" width="18" height="14" rx="2"/><path d="M3 7l9 6 9-6"/></svg></span>
    <span>Email:<br>hello@veyrahealth.org</span>
  </div>
  <div class="abs" style="left:127px;top:333px;width:946px;height:1px;background:#e2e6ea"></div>
  <p class="legal">© 2025 Copyright - Veyra Health Services. All Rights are Reserved.</p>
</footer>

</body>
</html>
```